Design a (20.4 x 10.14) Banner that says - Keep Hope Rising From Harvest Crown TV Family

We want a design (20.4 x 10.14) with the words 'Keep Hope Rising' as the main text and 'From Harvest Crown TV Family' underneath. For 'Harvest Crown TV', we'd like you to use the logo which can be found in the image attached.

The image attached is just an example but please let your creative juices flow!

Target Market(s)

Christian

Industry/Entity Type

Christian

Requirements
Must have
• Must have the words 'Keep Hope Rising' and 'From Harvest Crown TV Family'.

```html
<!DOCTYPE html>
<html lang="en">
<head>
<meta charset="utf-8">
<title>Keep Hope Rising – Harvest Crown TV Family Banner</title>
<link rel="stylesheet" href="https://fonts.googleapis.com/css2?family=Allura&family=Josefin+Sans:wght@700&family=Montserrat:wght@800;900&display=swap">
<style>
  :root {
    --stage: #ebebeb;
    --deep-purple: #2b2170;
    --mid-purple: #4a3ea8;
    --soft-purple: #6a63c8;
    --violet: #5b3fc0;
    --sky-blue: #2a8fd8;
    --brand-ink: #2e2a6e;
    --paper: #ffffff;
    --bar-grey: #d9d9e6;
  }
  html, body {
    margin: 0;
    width: 1200px;
    height: 849px;
    overflow: hidden;
    background: var(--stage);
  }
  .banner {
    position: absolute;
    left: 78px;
    top: 165px;
    width: 1044px;
    height: 518px;
    overflow: hidden;
    background: var(--deep-purple);
  }
  .banner-photo {
    position: absolute;
    inset: 0;
    background:
      radial-gradient(ellipse at 30% 45%, rgba(120,130,200,0.55), transparent 55%),
      radial-gradient(ellipse at 75% 60%, rgba(110,100,210,0.45), transparent 50%),
      linear-gradient(100deg, #35479a 0%, #4a4fb0 40%, #3b2e96 75%, #2a1d78 100%);
  }
  .banner-shapes {
    position: absolute;
    inset: 0;
  }
  .headline-script {
    position: absolute;
    left: 255px;
    top: 95px;
    font-family: "Allura", cursive;
    font-size: 200px;
    line-height: 1;
    color: rgba(255,255,255,0.92);
    transform: rotate(-12deg);
    transform-origin: left bottom;
  }
  .headline-block {
    position: absolute;
    right: 22px;
    top: 78px;
    text-align: right;
    font-family: "Josefin Sans", sans-serif;
    font-weight: 700;
    color: rgba(255,255,255,0.88);
    line-height: 0.84;
  }
  .headline-hope {
    display: block;
    font-size: 205px;
    letter-spacing: 10px;
    margin-right: -10px;
  }
  .headline-rising {
    display: block;
    font-size: 168px;
    letter-spacing: 2px;
    margin-top: 14px;
  }
  .signoff {
    position: absolute;
    left: 0;
    top: 330px;
    width: 330px;
    text-align: center;
    font-family: "Montserrat", sans-serif;
  }
  .signoff-label {
    display: block;
    font-weight: 900;
    font-size: 22px;
    letter-spacing: 3px;
    color: var(--sky-blue);
  }
  .signoff-brand {
    display: block;
    font-weight: 900;
    font-size: 30px;
    letter-spacing: -0.5px;
    color: var(--brand-ink);
    margin: 6px 0 6px;
  }
</style>
</head>
<body>
  <main class="banner">
    <div class="banner-photo" role="img" aria-label="Blue-violet tinted photograph of hands clasped together in prayer over a wooden table"></div>

    <svg class="banner-shapes" width="1044" height="518" viewBox="0 0 1044 518" aria-hidden="true">
      <rect class="accent-bar-purple" x="-10" y="214" width="120" height="16" rx="8" fill="var(--violet)"/>
      <rect class="accent-bar-light" x="-10" y="238" width="120" height="14" rx="7" fill="var(--bar-grey)"/>
      <path class="signoff-panel" d="M0 270 L500 462 Q540 478 552 505 L558 518 L0 518 Z" fill="var(--paper)"/>
      <path class="accent-bar-blue" d="M540 480 L690 480 Q700 480 700 490 L700 500 L560 500 Q545 500 540 490 Z" fill="var(--sky-blue)"/>
      <rect class="accent-bar-white" x="560" y="484" width="110" height="9" rx="4.5" fill="var(--paper)" opacity="0.85"/>
    </svg>

    <div class="headline-script">keep</div>
    <h1 class="headline-block" style="margin:0">
      <span class="headline-hope">HOPE</span>
      <span class="headline-rising">RISING</span>
    </h1>

    <div class="signoff">
      <span class="signoff-label">FROM</span>
      <span class="signoff-brand">Harvest Crown TV</span>
      <span class="signoff-label">FAMILY</span>
    </div>
  </main>
</body>
</html>
```